Fun and Flexible Word Template Design for Classroom Learning Resources

We're a global arts and education nonprofit based in New York. We're looking for a 2-page Word template design for our new collection of Learning Resources.
Page 1 of the template should include:
1. Lantern 9 logo (attached)
2. Resource title
3. Author photo
4. Author bio
5. Resource text
6. Sub-title text
7. Colored call-out box
Page 2 of the template should include:
2. Resource Title (in a smaller font)
3. Resource text
4. Sub-title text
5. Colored call-out box
The design must also adhere to our current brand guidelines: https://stylekit-demo.example/lantern-9
We've attached a very basic mock-up that includes the elements listed above. However, we encourage you to be more playful and/or creative with your design.
Our goal is to create a template that is flexible enough to accomodate a variety of resources (samples of 3 different resources are attached), that is also visually appealing enough to attract and hold the attention of busy educators.
Target Market(s)
Educators - Middle School, High School & College
Look and feel

```html
<!DOCTYPE html>
<html lang="en">
<head>
<meta charset="utf-8">
<title>Lantern 9 Learning Resource Template</title>
<link href="https://fonts.googleapis.com/css2?family=Bebas+Neue&family=Montserrat:wght@400;500;600;700&display=swap" rel="stylesheet">
<style>
  :root{
    --purple:#6b2d9b;
    --purple-bright:#7e3aa8;
    --purple-muted:#7a3db0;
    --navy:#1c1b46;
    --navy-deep:#15143a;
    --ink:#1d1d1f;
    --paper:#ffffff;
    --paper-shade:#e6e6ea;
    --stage:#ececf0;
    --photo-light:#c9c9c9;
    --photo-dark:#3a3a3a;
  }
  *{box-sizing:border-box;margin:0;padding:0}
  html,body{width:1050px;height:1200px;overflow:hidden}
  body{background:var(--stage);font-family:"Montserrat",sans-serif;color:var(--ink)}
  .canvas{position:relative;width:1050px;height:1200px}
  .page{
    position:absolute;top:247px;width:500px;height:706px;overflow:hidden;
    background:linear-gradient(160deg,var(--paper) 35%,var(--paper-shade) 70%,var(--paper) 100%);
    box-shadow:0 6px 24px rgba(20,20,50,.25);
  }
  .page--cover{left:17px}
  .page--continued{left:533px}

  /* cover header */
  .cover-header{position:absolute;left:0;top:0;width:500px;height:212px;
    background:linear-gradient(120deg,#3b1d70 0%,#5d2690 45%,#7a2f9c 65%,#4a2380 100%)}
  .cover-header__title{position:absolute;left:47px;top:30px;font-family:"Bebas Neue",sans-serif;
    font-size:84px;line-height:1;color:#fff;letter-spacing:.5px}
  .cover-header__subtitle{position:absolute;left:47px;top:127px;font-weight:700;font-size:24px;
    line-height:1.2;color:var(--purple-muted)}
  .bio-band{position:absolute;left:0;top:212px;width:500px;height:76px;background:var(--navy)}
  .bio-band__text{position:absolute;left:46px;top:12px;width:265px;font-weight:700;font-size:9.6px;
    line-height:1.42;color:#fff}
  .writer-photo{position:absolute;left:321px;top:128px;width:138px;height:138px;border-radius:50%;
    overflow:hidden;background:radial-gradient(circle at 50% 40%,var(--photo-light),var(--photo-dark))}
  .writer-photo__label{position:absolute;left:0;bottom:0;width:100%;height:30px;background:var(--purple);
    color:#fff;font-family:"Bebas Neue",sans-serif;font-size:15px;text-align:center;padding-top:4px}
  .writer-ring{position:absolute;left:310px;top:117px;width:160px;height:160px;border-radius:50%;
    border:1px solid rgba(160,110,220,.7)}

  /* text blocks */
  .section{position:absolute;left:26px;width:448px}
  .label{font-weight:700;font-size:11px;letter-spacing:.2px}
  .label--purple{color:var(--purple)}
  .body-text{font-size:8.6px;line-height:1.36;text-align:justify;margin-top:5px}
  .body-text + .body-text{margin-top:11px}

  .callout{position:absolute;left:0;top:404px;width:211px;height:302px;border-top-right-radius:22px;
    background:linear-gradient(180deg,#5a2a8e 0%,#3a2170 50%,var(--navy-deep) 100%)}
  .callout__text{position:absolute;left:26px;top:32px;width:160px;font-size:8.6px;line-height:1.36;color:#fff}
  .callout__text p + p{margin-top:11px}
  .callout__spacer{float:right;width:0;height:150px}
  .callout-photo{float:right;clear:right;width:104px;height:104px;margin-right:-39px;border-radius:50%;
    border:2px solid #fff;shape-outside:circle(50%);shape-margin:6px;
    background:radial-gradient(circle at 50% 40%,var(--photo-light),var(--photo-dark))}

  .column{position:absolute;left:233px;top:416px;width:241px}
  .column__kicker{font-weight:600;font-size:9px}
  .column__heading{font-weight:700;font-size:14px;color:var(--purple);margin-top:2px}

  .brand{position:absolute;right:26px;top:664px;display:flex;align-items:center;gap:7px}
  .brand__dot{width:26px;height:26px;border-radius:50%;background:var(--purple)}
  .brand__name{font-weight:600;font-size:11.5px;letter-spacing:.6px;color:var(--purple)}
  .foot-stripe{position:absolute;left:217px;bottom:0;width:283px;height:6px;background:var(--purple-bright)}

  /* continued page */
  .top-rule{position:absolute;left:0;top:0;width:500px;height:4px;background:var(--navy)}
  .top-rule--accent{top:5px;height:3px;background:var(--purple-bright)}
  .cont-title{position:absolute;left:26px;top:34px}
  .cont-title__kicker{font-weight:700;font-size:11px}
  .cont-title__heading{font-weight:700;font-size:18px;color:var(--purple);margin-top:2px}
</style>
</head>
<body>
<div class="canvas">

  <!-- Page 1 -->
  <section class="page page--cover">
    <header class="cover-header">
      <h1 class="cover-header__title">RESOURCE TITLE</h1>
      <p class="cover-header__subtitle">LOREM IPSUM<br>DOLOR</p>
    </header>
    <div class="bio-band">
      <p class="bio-band__text">Lorem ipsum dolor sit amet Lorem ipsum dolor sit amet Lorem ipsum dolor sit amet Lorem ipsum dolor sit amet Lorem ipsum dolor sit amet Lorem ipsum dolor sit amet</p>
    </div>
    <div class="writer-ring"></div>
    <div class="writer-photo" role="img" aria-label="Author portrait photo">
      <div class="writer-photo__label">WRITER PHOTO</div>
    </div>

    <div class="section" style="top:301px">
      <p class="label label--purple">RESOURCE TEXT</p>
      <p class="body-text">Lorem ipsum dolor sit amet, consectetur adipiscing elit. Morbi ut libero mattis, pellentesque urna eu, iaculis lorem. Interdum et malesuada fames ac ante ipsum primis in faucibus. Duis pellen- tesque orci consectetur sapien vulputate imperdiet. Aliquam erat volutpat. Integer tristique erat lorem, sed posuere enim rhoncus sed. Fusce ut venenatis nulla, sed elementum arcu. Maecenas eu- ismod mauris euismod augue posuere venenatis. Duis id porta ante integer.</p>
    </div>

    <aside class="callout">
      <div class="callout__text">
        <span class="callout__spacer"></span>
        <span class="callout-photo" role="img" aria-label="Author photo"></span>
        <p>Lorem ipsum dolor sit amet, consectetur adipiscing elit. Morbi ut libero mattis, pellentesque urna eu, iaculis lorem. Interdum et malesuada fames ac ante ipsum primis in faucibus. Duis pellen- tesque orci consectetur sapien vulputate imperdiet. Aliquam erat volutpat.</p>
        <p>Integer tristique erat lorem, sed posuere enim rhoncus sed. Fusce ut venenatis nulla, sed elemen- tum arcu. Maecenas eu- ismod mauris euis- mod augue posuere venenatis. Duis id porta ante integer.</p>
      </div>
    </aside>

    <div class="column">
      <p class="column__kicker">SUB-HEADER TEXT -</p>
      <h2 class="column__heading">LOREM IPSUM DOLOR SIT</h2>
      <p class="body-text">Lorem ipsum dolor sit amet, consectetur adipiscing elit. Morbi ut libero mattis, pellentesque urna eu, iaculis lorem. Interdum et malesuada fames ac ante ipsum primis in faucibus. Duis pellen- tesque orci consectetur sapien vulputate imperdiet. Aliquam erat volutpat. Integer tristique erat lorem, sed posuere enim rhoncus sed.</p>
      <p class="body-text">Fusce ut venenatis nulla, sed elementum arcu. Maecenas eu- ismod mauris euismod augue posuere venenatis. Duis id porta ante integer.</p>
      <p class="body-text">Fusce ut venenatis nulla, sed elementum arcu. Maecenas eu- ismod mauris euismod augue posuere venenatis. Duis id porta ante integer. Fusce ut venenatis nulla, sed elementum arcu.</p>
    </div>

    <div class="brand"><span class="brand__dot"></span><span class="brand__name">LANTERN 9</span></div>
    <div class="foot-stripe"></div>
  </section>

  <!-- Page 2 -->
  <section class="page page--continued">
    <div class="top-rule"></div>
    <div class="top-rule top-rule--accent"></div>
    <div class="cont-title">
      <p class="cont-title__kicker">RESOURCE TITLE TEXT</p>
      <h1 class="cont-title__heading">LOREM IPSUM DOLOR SIT (CONT’D)</h1>
    </div>

    <div class="section" style="top:93px">
      <p class="label">RESOURCE TEXT</p>
      <p class="body-text">Lorem ipsum dolor sit amet, consectetur adipiscing elit. Morbi ut libero mattis, pellentesque urna eu, iaculis lorem. Interdum et malesuada fames ac ante ipsum primis in faucibus. Duis pellen- tesque orci consectetur sapien vulputate imperdiet. Aliquam erat volutpat. Integer tristique erat lorem, sed posuere enim rhoncus sed. Fusce ut venenatis nulla, sed elementum arcu. Maecenas eu- ismod mauris euismod augue posuere venenatis.</p>
      <p class="body-text">Lorem ipsum dolor sit amet, consectetur adipiscing elit. Morbi ut libero mattis, pellentesque urna eu, iaculis lorem. Interdum et malesuada fames ac ante ipsum primis in faucibus. Duis pellen- tesque orci consectetur sapien vulputate imperdiet. Aliquam erat volutpat. Integer tristique erat lorem, sed posuere enim rhoncus sed. Fusce ut venenatis nulla, sed elementum arcu. Maecenas eu- ismod mauris euismod augue posuere venenatis.</p>
      <p class="body-text">Lorem ipsum dolor sit amet, consectetur adipiscing elit. Morbi ut libero mattis, pellentesque urna eu, iaculis lorem. Interdum et malesuada fames ac ante ipsum primis in faucibus. Duis pellen- tesque orci consectetur sapien vulputate imperdiet. Aliquam erat volutpat. Integer tristique erat lorem, sed posuere enim rhoncus sed. Fusce ut venenatis nulla, sed elementum arcu. Maecenas eu- ismod mauris euismod augue posuere venenatis.</p>
      <p class="body-text">Lorem ipsum dolor sit amet, consectetur adipiscing elit. Morbi ut libero mattis, pellentesque urna eu, iaculis lorem. Interdum et malesuada fames ac ante ipsum primis in faucibus. Duis pellen- tesque orci consectetur sapien vulputate imperdiet. Aliquam erat volutpat. Integer tristique erat lorem, sed posuere enim rhoncus sed. Fusce ut venenatis nulla, sed elementum arcu. Maecenas eu- ismod mauris euismod augue posuere venenatis.</p>
    </div>

    <aside class="callout">
      <div class="callout__text">
        <span class="callout__spacer"></span>
        <span class="callout-photo" role="img" aria-label="Author photo"></span>
        <p>Lorem ipsum dolor sit amet, consectetur adipiscing elit. Morbi ut libero mattis, pellentesque urna eu, iaculis lorem. Interdum et malesuada fames ac ante ipsum primis in faucibus. Duis pellen- tesque orci consectetur sapien vulputate imperdiet. Aliquam erat volutpat.</p>
        <p>Integer tristique erat lorem, sed posuere enim rhoncus sed. Fusce ut venenatis nulla, sed elemen- tum arcu. Maecenas eu- ismod mauris euis- mod augue posuere venenatis. Duis id porta ante integer.</p>
      </div>
    </aside>

    <div class="column">
      <p class="column__kicker">SUB-HEADER TEXT -</p>
      <h2 class="column__heading">LOREM IPSUM DOLOR SIT</h2>
      <p class="body-text">Lorem ipsum dolor sit amet, consectetur adipiscing elit. Morbi ut libero mattis, pellentesque urna eu, iaculis lorem. Interdum et malesuada fames ac ante ipsum primis in faucibus.</p>
      <p class="body-text">Duis pellen- tesque orci consectetur sapien vulputate imperdiet.</p>
      <p class="body-text">Aliquam erat volutpat. Integer tristique erat lorem, sed posuere enim rhoncus sed. Fusce ut venenatis nulla, sed elementum arcu. Maecenas eu- ismod mauris euismod augue posuere venenatis. Duis id porta ante integer.</p>
    </div>

    <div class="brand"><span class="brand__dot"></span><span class="brand__name">LANTERN 9</span></div>
    <div class="foot-stripe"></div>
  </section>

</div>
</body>
</html>
```